Legislative compliance to home owners, landlords and agents

Logo, business card and stationaly header for a sole trader offering sevices in the UK to home owners, landlords and Letting agents to meet legislation requirement relating to sale and leasing of rental domestic homes. Services offered include Legionella Risk Assessment, Portable Appliance Testing and Energy Performance Certificates. Logo to include depiction of a house and compliance tick list images. Have an existing card with water splash image to reflect water testing, so considering picking up same wave blue. Company name Talvane Property Services. Web www.talvaneps-example.com. email: info@talvaneps-example.com. Address: Glenmorrow, Aberdeen. All three services to be listed. Name as existing card.,

Target Market(s)

UK home owners, landlords, lettings and estate agents

Industry/Entity Type

Property Management

Contact Information for Business Card

Derek Hollingsby CEng, MSoHTF
Address: Glenmorrow, Aberdeen
Web: www.talvaneps-example.com
e-mail info@talvaneps-example.com
Phone: 07921 458 302
Services: Legionella Risk Assessment, Portable Appliance Testing, Energy Performance Certificate

Logo Text

Talvane Property Services

Font styles to use
Sans Serif

Colors

Designer to choose colors to be used in the design.

Requirements
Must have
• Suitable for standard UK business card size 85 mm x 55 mm, with allowance for safety border/ bleed such that colours extend to outside border of card once printed
Nice to have
• Clear font style and layout
• Happy to see images depicting phone, address etc

```html
<!DOCTYPE html>
<html lang="en">
<head>
<meta charset="utf-8">
<title>Talvane Property Services – Business Card</title>
<link rel="stylesheet" href="https://fonts.googleapis.com/css2?family=Roboto:wght@400;500;700&display=swap">
<style>
  :root {
    --navy: #262f6b;
    --wave-blue: #3aa9df;
    --ink: #333a4a;
    --paper: #ffffff;
    --backdrop: #e9eaee;
  }
  * { box-sizing: border-box; margin: 0; padding: 0; }
  html, body {
    width: 1200px; height: 900px; overflow: hidden;
    background: var(--backdrop);
    font-family: "Roboto", Arial, sans-serif;
  }
  .stage {
    width: 1200px; height: 900px;
    display: flex; align-items: center; justify-content: center; gap: 50px;
  }
  .card {
    position: relative;
    width: 544px; height: 352px;
    background: var(--paper);
    box-shadow: 0 6px 22px rgba(20, 25, 50, 0.18);
    overflow: hidden;
  }

  /* Front */
  .services-band {
    position: absolute; left: 0; right: 0; top: 34px; height: 34px;
    background: var(--navy);
    color: var(--paper);
    font-size: 14px; letter-spacing: 0.2px;
    display: flex; align-items: center; padding-left: 34px;
  }
  .contact-list {
    position: absolute; left: 30px; top: 96px;
    list-style: none;
    font-size: 14px; color: var(--ink);
  }
  .contact-list li { display: flex; align-items: center; gap: 10px; height: 25px; }
  .contact-icon { width: 16px; height: 16px; flex: none; }
  .holder {
    position: absolute; right: 34px; top: 92px; text-align: left;
  }
  .holder-name { font-size: 24px; font-weight: 500; color: var(--navy); }
  .holder-credentials { font-size: 18px; color: var(--wave-blue); margin-top: 2px; }
  .company-mark {
    position: absolute; display: flex; align-items: center; gap: 10px;
    font-weight: 700; color: var(--navy); white-space: nowrap;
  }
  .company-mark .mark-square { width: 16px; height: 16px; background: var(--wave-blue); flex: none; }
  .front .company-mark { right: 34px; bottom: 42px; font-size: 21px; }

  /* Back */
  .corner-bar { position: absolute; height: 34px; background: var(--navy); }
  .corner-bar.top { left: 0; top: 0; width: 150px; }
  .corner-bar.bottom { right: 0; bottom: 0; width: 200px; }
  .back .company-mark {
    left: 50%; top: 50%; transform: translate(-50%, -50%); font-size: 27px;
  }
</style>
</head>
<body>
<main class="stage">

  <section class="card front" aria-label="Business card front">
    <div class="services-band">Legionella Risk Assessment, Portable Appliance Testing, Energy Performance Certificate</div>

    <ul class="contact-list">
      <li>
        <svg class="contact-icon" viewBox="0 0 16 16" aria-hidden="true"><circle cx="8" cy="8" r="7.2" fill="none" stroke="var(--wave-blue)" stroke-width="1.3"/><path d="M5.4 4.6l1.4-.3.7 1.7-.9.7a5 5 0 0 0 2.7 2.7l.7-.9 1.7.7-.3 1.4c-3.5.2-6.3-2.6-6-6z" fill="var(--wave-blue)"/></svg>
        07921 458 302
      </li>
      <li>
        <svg class="contact-icon" viewBox="0 0 16 16" aria-hidden="true"><circle cx="8" cy="8" r="7.2" fill="none" stroke="var(--wave-blue)" stroke-width="1.3"/><rect x="4.3" y="5.4" width="7.4" height="5.2" fill="none" stroke="var(--wave-blue)" stroke-width="1.1"/><path d="M4.3 5.6L8 8.4l3.7-2.8" fill="none" stroke="var(--wave-blue)" stroke-width="1.1"/></svg>
        e-mail info@talvaneps-example.com
      </li>
      <li>
        <svg class="contact-icon" viewBox="0 0 16 16" aria-hidden="true"><circle cx="8" cy="8" r="7.2" fill="none" stroke="var(--wave-blue)" stroke-width="1.3"/><path d="M8 12.2s-2.8-3-2.8-5A2.8 2.8 0 0 1 10.8 7.2c0 2-2.8 5-2.8 5z" fill="var(--wave-blue)"/><circle cx="8" cy="7.1" r="1" fill="var(--paper)"/></svg>
        Glenmorrow, Aberdeen
      </li>
      <li>
        <svg class="contact-icon" viewBox="0 0 16 16" aria-hidden="true"><circle cx="8" cy="8" r="7.2" fill="none" stroke="var(--wave-blue)" stroke-width="1.3"/><circle cx="8" cy="8" r="3.6" fill="none" stroke="var(--wave-blue)" stroke-width="1"/><path d="M4.4 8h7.2M8 4.4c-1.6 2.2-1.6 5 0 7.2M8 4.4c1.6 2.2 1.6 5 0 7.2" fill="none" stroke="var(--wave-blue)" stroke-width="0.9"/></svg>
        www.talvaneps-example.com
      </li>
    </ul>

    <div class="holder">
      <p class="holder-name">Derek Hollingsby</p>
      <p class="holder-credentials">CEng, MSoHTF</p>
    </div>

    <div class="company-mark"><span>Talvane Property Services</span><span class="mark-square"></span></div>
  </section>

  <section class="card back" aria-label="Business card back">
    <div class="corner-bar top"></div>
    <div class="company-mark"><span>Talvane Property Services</span><span class="mark-square"></span></div>
    <div class="corner-bar bottom"></div>
  </section>

</main>
</body>
</html>
```